Boutique winery needs new wine label

domaine Verlin is a boutique wine company based in the Clare Valley of South Australia. We are an established brand, best known for our Riesling and Grenache. We plan to launch a new sub brand called La Douce ferme and require a new label that is different from the others we use. It will be used on small batch Riesling and should have a rustic but quality feel. Attached is a small image of the house where the winery is based. The label should incorporate a hand drawn sketch of the house.
Target Market(s)
High end wine consumers with an interest in Riesling
Requirements
Must have
- hand drawn sketch of the house
- the name of the wine La Douce ferme present on the front label
- Vintage (2018) and region (Clare Valley) present on the front label
- Minimal use of colour on the label but would look at embellishments such as gold foil
Nice to have
- A clean, simple style of label, preferably with white background
- La Douce ferme written in script style
Should not have
- domaine Verlin written on the front label
- the current domaine Verlin logo

```html
<!DOCTYPE html>
<html lang="en">
<head>
<meta charset="utf-8">
<title>La Douce ferme — Clare Valley Riesling 2018</title>
<link rel="stylesheet" href="https://fonts.googleapis.com/css2?family=Parisienne&family=Cormorant+Garamond:wght@600&family=Montserrat:wght@500&display=swap">
<style>
  :root {
    --frame-black: #000000;
    --frame-grey: #666666;
    --label-white: #ffffff;
    --ink: #231a1a;
    --sketch-tone-light: #d9d6d4;
    --sketch-tone-dark: #8f8a88;
  }
  html, body {
    margin: 0;
    padding: 0;
    width: 1200px;
    height: 950px;
    overflow: hidden;
    background: var(--frame-black);
  }
  .label {
    position: relative;
    width: 1200px;
    height: 950px;
    background: var(--frame-black);
  }
  .label__band {
    position: absolute;
    left: 63px;
    top: 58px;
    width: 1075px;
    height: 835px;
    background: var(--frame-grey);
  }
  .label__face {
    position: absolute;
    left: 82px;
    top: 77px;
    width: 1037px;
    height: 797px;
    background: var(--label-white);
  }
  .house-sketch {
    position: absolute;
    left: 251px;
    top: 46px;
    width: 543px;
    height: 330px;
    border-radius: 4px;
    background: linear-gradient(180deg, var(--sketch-tone-light) 0%, var(--sketch-tone-dark) 100%);
  }
  .wine-name {
    position: absolute;
    left: 0;
    right: 0;
    top: 400px;
    margin: 0;
    text-align: center;
    font-family: "Parisienne", cursive;
    font-weight: 400;
    font-size: 118px;
    line-height: 1;
    color: var(--ink);
  }
  .region {
    position: absolute;
    left: 0;
    right: 0;
    top: 583px;
    margin: 0;
    text-align: center;
    font-family: "Cormorant Garamond", serif;
    font-weight: 600;
    font-size: 36px;
    letter-spacing: 0.3em;
    padding-left: 0.3em;
    color: var(--ink);
  }
  .variety {
    position: absolute;
    left: 0;
    right: 0;
    top: 667px;
    margin: 0;
    text-align: center;
    font-family: "Montserrat", sans-serif;
    font-weight: 500;
    font-size: 25px;
    letter-spacing: 0.3em;
    padding-left: 0.3em;
    color: var(--ink);
  }
  .vintage {
    position: absolute;
    left: 0;
    right: 0;
    top: 727px;
    margin: 0;
    text-align: center;
    font-family: "Montserrat", sans-serif;
    font-weight: 500;
    font-size: 21px;
    letter-spacing: 0.2em;
    padding-left: 0.2em;
    color: var(--ink);
  }
</style>
</head>
<body>
  <div class="label">
    <div class="label__band"></div>
    <main class="label__face">
      <div class="house-sketch" role="img" aria-label="Hand-drawn ink sketch of the two-storey winery house with shuttered windows, a small balcony and ivy-covered walls"></div>
      <h1 class="wine-name">La Douce ferme</h1>
      <p class="region">CLARE VALLEY</p>
      <p class="variety">RIESLING</p>
      <p class="vintage">2018</p>
    </main>
  </div>
</body>
</html>
```